Redesign Of Current Landing Page

I need to redesign this landing page https://www.brightoakpromos.biz/?page=landing&landing=23 (Please do not opt in because when you do it will show you the home page. Please clear your cookies before going to this url above to view the 1 page landing page.)

Please use my updated website as a reference for colors and logo.
http://layoutcraftzone.com/dh/bopg/index.html

I would like the call to action to be a button that opens into a lead form...

Button would be "Download Samples"

small business owners

Marketing

1 page

Designer to choose colors to be used in the design.

• must be full responsive on all devices
• must have a legitimate professional apeal to it
• open

```html
<!DOCTYPE html>
<html lang="en">
<head>
<meta charset="utf-8">
<title>Bright Oak Promos – Attract More Customers</title>
<link rel="stylesheet" href="https://fonts.googleapis.com/css2?family=Raleway:wght@500;600;700&family=Roboto:wght@400;500;700&display=swap">
<style>
:root{
  --blue:#0b72c4;
  --blue-deep:#0d2440;
  --navy:#1c2536;
  --orange:#fbaa13;
  --white:#ffffff;
  --ink:#333a44;
  --grey-text:#6c6f74;
  --card-grey:#eeeeee;
  --footer:#1f1f1f;
  --rule:#e6e6e6;
}
*{box-sizing:border-box;margin:0;padding:0}
html,body{width:1200px;height:2184px;overflow:hidden;background:var(--white)}
body{font-family:"Roboto",Arial,sans-serif;color:var(--ink);position:relative}
.btn-cta{position:absolute;display:flex;flex-direction:column;align-items:center;justify-content:center;width:258px;height:56px;background:var(--orange);color:var(--white);text-decoration:none;border-radius:2px;font-family:"Raleway",Arial,sans-serif;line-height:1.05}
.btn-cta .main{font-size:18px;font-weight:700;letter-spacing:.2px}
.btn-cta .sub{font-size:13px;font-weight:700}
.brand{position:absolute;display:flex;align-items:center;gap:10px;font-family:"Raleway",Arial,sans-serif;font-weight:700;color:var(--blue);font-size:30px;letter-spacing:.5px}
.brand .mark{width:30px;height:30px;background:var(--blue)}
/* hero */
.hero{position:absolute;left:0;top:0;width:1200px;height:658px;overflow:hidden}
.hero-photo{position:absolute;inset:0;background:linear-gradient(135deg,#1d3a5e 0%,#16304f 45%,#0f2036 100%)}
.hero .brand{left:112px;top:34px}
.phone{position:absolute;left:628px;top:28px;display:flex;gap:12px;color:var(--white)}
.phone-num{font-size:21px;font-weight:700;line-height:1.1}
.phone-hours{font-size:15px}
.hero .btn-cta{left:831px;top:26px}
.hero-title{position:absolute;left:0;width:1200px;top:146px;text-align:center}
.hero-title h1{display:inline-block;border-top:1px solid rgba(255,255,255,.7);padding-top:10px;font-family:"Raleway",Arial,sans-serif;font-weight:600;font-size:31px;color:var(--white);padding-left:4px;padding-right:4px}
.hero-sub{position:absolute;left:0;width:1200px;top:224px;text-align:center;color:var(--white);font-size:17px;line-height:24px;letter-spacing:.4px}
.hero-disc{position:absolute;left:360px;top:418px;width:480px;height:480px;border-radius:50%;background:var(--blue);box-shadow:0 0 0 10px rgba(11,114,196,.25)}
.hero-samples{position:absolute;left:410px;top:340px;width:390px;height:318px;background:linear-gradient(160deg,#c9d6e4,#7a93b2 55%,#36536f);border-radius:4px}
/* imagine */
.story{position:absolute;left:0;top:658px;width:1200px;height:400px;overflow:hidden}
.story-photo{position:absolute;inset:0;background:linear-gradient(180deg,#243044,#1c2536 60%,#232c3d)}
.story-col{position:absolute;top:64px;width:470px;color:var(--white)}
.story-col.left{left:112px}
.story-col.right{left:626px}
.story-divider{position:absolute;left:600px;top:56px;width:1px;height:290px;background:rgba(255,255,255,.2)}
.story-col h2{font-family:"Raleway",Arial,sans-serif;font-weight:600;font-size:23px;margin-bottom:14px}
.story-col p{font-size:13px;line-height:20px;margin-bottom:21px}
/* reasons */
.reasons-btn-1{left:470px;top:1111px}
.reasons-title{position:absolute;left:0;width:1200px;top:1212px;text-align:center;font-family:"Raleway",Arial,sans-serif;font-weight:600;font-size:23px;color:var(--ink)}
.reasons{position:absolute;left:112px;top:1268px;display:flex;gap:16px}
.reason{width:150px;height:192px;background:var(--card-grey)}
.reason-top{height:100px;background:var(--blue);position:relative;display:flex;align-items:center;justify-content:center}
.reason-top::after{content:"";position:absolute;left:0;bottom:-6px;width:100%;height:10px;background:linear-gradient(175deg,var(--orange) 50%,transparent 52%)}
.reason-top svg{width:54px;height:54px}
.reason p{padding:18px 10px 0;text-align:center;font-size:13px;line-height:19px;color:var(--grey-text)}
.reasons-btn-2{left:470px;top:1511px}
.section-rule{position:absolute;left:0;top:1619px;width:1200px;height:1px;background:var(--rule)}
/* testimonial */
.client-photo{position:absolute;left:68px;top:1645px;width:398px;height:399px;background:linear-gradient(180deg,#f3f3f3,#e4e4e4 60%,#b8bcc2)}
.testimonial-title{position:absolute;left:446px;top:1664px;font-family:"Raleway",Arial,sans-serif;font-weight:600;font-size:23px;color:var(--ink)}
.quote-mark{position:absolute;left:446px;top:1740px}
.quote{position:absolute;left:504px;top:1736px;width:584px}
.quote p{font-size:13px;line-height:21px;color:var(--grey-text)}
.quote .name{margin-top:20px;color:var(--blue);font-weight:500;font-size:15px}
.quote .place{font-size:14px;color:var(--grey-text)}
/* footer */
.site-footer{position:absolute;left:0;top:2044px;width:1200px;height:140px;background:var(--footer)}
.site-footer .brand{left:112px;top:36px;color:#8a8f96;font-size:24px}
.site-footer .brand .mark{width:24px;height:24px;background:#8a8f96}
.socials{position:absolute;left:112px;top:80px;display:flex;gap:8px}
.socials span{width:30px;height:30px;border-radius:50%;border:2px solid #6f7378}
.legal{position:absolute;left:239px;top:82px;color:#8a8f96;font-size:13px;line-height:20px}
.site-footer .btn-cta{left:831px;top:43px}
</style>
</head>
<body>

<header class="hero">
  <div class="hero-photo" role="img" aria-label="Dimmed photo of a business team meeting around a boardroom table"></div>
  <div class="brand"><span class="mark"></span>Bright Oak Promos</div>
  <div class="phone">
    <svg width="22" height="36" viewBox="0 0 22 36" fill="none" stroke="#fff" stroke-width="2"><rect x="1" y="1" width="20" height="34" rx="3"/><line x1="8" y1="30" x2="14" y2="30"/></svg>
    <div><div class="phone-num">1-800-555-0142</div><div class="phone-hours">Mon-Fri 8am-5pm PST</div></div>
  </div>
  <a class="btn-cta" href="#"><span class="main">DOWNLOAD FREE SAMPLES</span><span class="sub">OF OUR INCENTIVES</span></a>
  <div class="hero-title"><h1>ATTRACT MORE CUSTOMERS</h1></div>
  <p class="hero-sub">WHO SPEND MORE MONEY WITH YOUR BUSINESS MORE OFTEN USING<br>FREE VACATION &amp; CRUISE CERTIFICATES AND OTHER INCENTIVES<br>WITHOUT BREAKING THE BANK!</p>
  <div class="hero-disc"></div>
  <div class="hero-samples" role="img" aria-label="Fanned stack of sample incentive certificates for cruises, cash back, hotel stays and electronics"></div>
</header>

<section class="story">
  <div class="story-photo" role="img" aria-label="Dark tinted photo of colleagues working at a desk"></div>
  <div class="story-divider"></div>
  <div class="story-col left">
    <h2>IMAGINE</h2>
    <p>Being able to create exciting give away promotions that will boost your sales without ever having to worry about cost.</p>
    <p>Bright Oak Promo Group, Inc. provides high-perceived value promotional incentives to businesses that want to advertise an exciting Give Away that will instantly attract more customers from your existing advertising efforts.</p>
    <p>Your business can give away incentive certificates that are redeemable for luxury hotel &amp; resort stays with airfare included, cruises, cash for gas, groceries, dining and even electronic goods.</p>
  </div>
  <div class="story-col right">
    <h2>HOW CAN WE DO IT?</h2>
    <p>Being able to create exciting give away promotions that will boost your sales without ever having to worry about cost.</p>
    <p>Bright Oak Promo Group, Inc. provides high-perceived value promotional incentives to businesses that want to advertise an exciting Give Away that will instantly attract more customers from your existing advertising efforts.</p>
    <p>Your business can give away incentive certificates that are redeemable for luxury hotel &amp; resort stays with airfare included, cruises, cash for gas, groceries, dining and even electronic goods.</p>
  </div>
</section>

<a class="btn-cta reasons-btn-1" href="#"><span class="main">DOWNLOAD FREE SAMPLES</span><span class="sub">OF OUR INCENTIVES</span></a>
<h2 class="reasons-title">WHY OFFER INCENTIVES TO CUSTOMERS?</h2>
<div class="reasons">
  <div class="reason"><div class="reason-top"><svg viewBox="0 0 54 54" fill="#fff"><rect x="4" y="40" width="6" height="10"/><rect x="14" y="34" width="6" height="16"/><rect x="24" y="26" width="6" height="24"/><rect x="34" y="18" width="6" height="32"/><rect x="44" y="8" width="6" height="42"/><path d="M4 34 L30 12" stroke="#fff" stroke-width="3" fill="none"/><path d="M24 10 L33 9 L31 18 Z"/></svg></div><p>Increase Responses From Your Existing Ads</p></div>
  <div class="reason"><div class="reason-top"><svg viewBox="0 0 54 54" fill="#fff"><path d="M40 4a12 12 0 0 0-12 15L6 41a5 5 0 0 0 7 7l22-22A12 12 0 0 0 50 14l-7 7-7-3-2-7 7-7z"/></svg></div><p>#1 Sales Closing Tool - Gift w/ Purchase</p></div>
  <div class="reason"><div class="reason-top"><svg viewBox="0 0 54 54" fill="#fff"><path d="M27 3l7 15 16 2-12 11 3 17-14-8-14 8 3-17L4 20l16-2z"/></svg></div><p>Build Brand Awareness and Trust</p></div>
  <div class="reason"><div class="reason-top"><svg viewBox="0 0 54 54" fill="#fff"><circle cx="33" cy="15" r="9"/><path d="M18 50c0-14 6-22 15-22s15 8 15 22z"/><circle cx="20" cy="18" r="8" stroke="#0b72c4" stroke-width="2"/><path d="M4 50c0-12 6-20 16-20s14 8 14 20z" stroke="#0b72c4" stroke-width="2"/></svg></div><p>Insure The Sale Over Your Competition</p></div>
  <div class="reason"><div class="reason-top"><svg viewBox="0 0 54 54" fill="none" stroke="#fff" stroke-width="4"><path d="M6 18h40M36 8l10 10-10 10"/><path d="M48 38H8M18 28L8 38l10 10"/></svg></div><p>Boost Repeat and Referral Business</p></div>
  <div class="reason"><div class="reason-top"><svg viewBox="0 0 54 54"><circle cx="27" cy="27" r="24" fill="#fff"/><circle cx="27" cy="27" r="18" fill="none" stroke="#0b72c4" stroke-width="3"/><text x="27" y="36" text-anchor="middle" font-family="Roboto,Arial,sans-serif" font-weight="700" font-size="26" fill="#0b72c4">$</text></svg></div><p>Improve Retention Rates</p></div>
</div>
<a class="btn-cta reasons-btn-2" href="#"><span class="main">DOWNLOAD FREE SAMPLES</span><span class="sub">OF OUR INCENTIVES</span></a>
<div class="section-rule"></div>

<section>
  <div class="client-photo" role="img" aria-label="Portrait of a smiling businessman in a grey suit with arms crossed"></div>
  <h2 class="testimonial-title">WHAT ABOUT OUR CLIENT SAYS</h2>
  <svg class="quote-mark" width="38" height="30" viewBox="0 0 38 30" fill="#0b72c4"><path d="M0 30V16C0 7 5 1 14 0v6c-4 1-6 4-6 8h7v16zM21 30V16c0-9 5-15 14-16v6c-4 1-6 4-6 8h7v16z"/></svg>
  <div class="quote">
    <p>I began using your incentives two years ago to boost lead generation efforts. I have experienced a 63% increase in lead captures. And, even more importantly, my sales have increased as well. The ability to offer unlimited certificates and not having to pay for each certificate I give away is perhaps the best feature of the program, but having the flexibility to email or print certificates for my customers is also wonderful. I even use your html banners to automate my promotions right on my website!,</p>
    <p class="name">Dan R.</p>
    <p class="place">Fairview, OH</p>
  </div>
</section>

<footer class="site-footer">
  <div class="brand"><span class="mark"></span>Bright Oak Promos</div>
  <div class="socials"><span></span><span></span><span></span></div>
  <div class="legal">© 2017 Bright Oak Promo Group, Inc. All Rights Reserved<br>Terms of Use &nbsp;|&nbsp; Privacy Policy</div>
  <a class="btn-cta" href="#"><span class="main">DOWNLOAD FREE SAMPLES</span><span class="sub">OF OUR INCENTIVES</span></a>
</footer>

</body>
</html>
```